Business Card Design and Logo Needed

I need Business Cards and a Logo for my website and public speaking business which can be found at: www.talia-ferrow.com

I'm looking for creative and unique ideas. Some business cards I've found online that I like can be found at:
http://gigmarketloft.com/general/18-smokin-hot-business-card-designs/

and at

http://www.theprintnookery.com/2009/04/50-creative-business-cards-of-50-graphic-designers/

```html
<!DOCTYPE html>
<html lang="en">
<head>
<meta charset="utf-8">
<title>Talia Ferrow — Business Card</title>
<link href="https://fonts.googleapis.com/css2?family=Ubuntu:wght@300;400;700&display=swap" rel="stylesheet">
<style>
  :root {
    --plum: #7b2a7e;
    --plum-soft: #9a5a9c;
    --paper: #ffffff;
    --backdrop: #ece8e2;
    --ink-light: #ffffff;
  }
  * { margin: 0; padding: 0; box-sizing: border-box; }
  html, body {
    width: 1200px; height: 843px; overflow: hidden;
    background: var(--backdrop);
    font-family: "Ubuntu", sans-serif;
  }
  .canvas { position: relative; width: 1200px; height: 843px; }

  .card {
    position: absolute; top: 299px;
    width: 532px; height: 267px;
    background: var(--plum);
    overflow: hidden;
  }
  .card--front { left: 57px; }
  .card--back { left: 612px; }

  /* Front: white identity strip */
  .identity-strip {
    position: absolute; left: 0; top: 0;
    width: 166px; height: 100%;
    background: var(--paper);
  }
  .brand-mark {
    position: absolute; left: 18px; top: 12px;
    width: 76px; height: 76px;
  }
  /* Horizontal block rotated to read bottom-to-top; name left, tagline right */
  .identity {
    position: absolute; left: 36px; top: 143px;
    width: 150px; height: 36px;
    transform: rotate(-90deg);
    transform-origin: 50% 50%;
    color: var(--plum);
    text-align: center;
    white-space: nowrap;
  }
  .identity__name {
    display: block;
    font-weight: 300; font-size: 22px; letter-spacing: 0.3px;
    line-height: 24px;
  }
  .identity__role {
    display: block;
    font-size: 7.5px; line-height: 12px;
  }

  /* Front: contact block */
  .contact {
    position: absolute; left: 200px; top: 87px;
    color: var(--ink-light);
    font-size: 14px; line-height: 19px;
  }
  .contact__address { margin-bottom: 18px; }
  .contact__list { list-style: none; margin-bottom: 18px; }
  .contact__label { font-weight: 700; }
  .contact__web { font-weight: 700; }

  /* Back */
  .back-name {
    position: absolute; left: 0; right: 0; top: 50%;
    transform: translateY(-50%);
    text-align: center;
    color: var(--plum-soft);
    font-weight: 300; font-size: 26px; letter-spacing: 0.5px;
  }
</style>
</head>
<body>
<main class="canvas">
  <section class="card card--front" aria-label="Business card front">
    <div class="identity-strip">
      <svg class="brand-mark" viewBox="0 0 80 80" aria-hidden="true">
        <circle cx="40" cy="40" r="36" fill="none" stroke="var(--plum)" stroke-width="2"/>
      </svg>
      <div class="identity">
        <span class="identity__name">Talia Ferrow</span>
        <span class="identity__role">Public Speaker &amp; Philanthropist</span>
      </div>
    </div>

    <div class="contact">
      <p class="contact__address">2190 Larkmoor Avenue, Suite 410<br>Brookvale, Texas 75099</p>
      <ul class="contact__list">
        <li><span class="contact__label">Phone</span> 555 214 0386</li>
        <li><span class="contact__label">Fax</span> 555 214 0391</li>
        <li><span class="contact__label">Email</span> info@taliaferrow.com</li>
      </ul>
      <p class="contact__web">www.talia-ferrow.com</p>
    </div>
  </section>

  <section class="card card--back" aria-label="Business card back">
    <p class="back-name">Talia Ferrow</p>
  </section>
</main>
</body>
</html>
```